"Steady Frame Slim Down Roadmap" eBook cover

THE TITLE HAS CHANGED SLIGHTLY TO ;
"Steady Frame Slim Down Roadmap"

The following is for a fat loss, health and fitness eBook titled "Steady Frame Slim Down Roadmap." This design should help promote and market this product, as well as intrigue those to not only make a purchase... but want to very much participate in the material and follow the material!

There is no restriction of color, idea, etc. PLEASE help me with your expertise in developing a great cover for this project...

THANKS SO MUCH

This book separates others just by the quality information provided. To much trial and error is wasted on false claims and overrated programs....I have provided the books topics below to hopefully give you a better understanding;
CHAPTER 1
Steady Frame Slimdown Manual
- What is it?
- Why it works?
- Why it will work for you?
CHAPTER 2
Kill Cardio
- Why cardio sucks?
- Myth about cardio?
- What cardio works for fat loss
CHAPTER 3
Iron vs. Machine
- What type of resistance training is best for fat loss?
- Why?
- The big pitfall to working on machines?
CHAPTER 4
Should You Really Eat That?
- Foods that build muscle
- Foods that burn fat
- Foods that suck!
CHAPTER 5
Playing With Iron
- Playing with iron
- 17 upper body builders
- 17 lower body builders
- 11 workouts in 11 minutes
CHAPTER 6
Buying Equipment On A Budget
- How to find dirt cheap dumbbells?
- How to build equipment under $100

THANKS AGAIN!

Target Market(s)

Self-Help / Health And Fitness / Nutrition

Industry/Entity Type

Health And Wellness

Font styles to use
Serif
Sans Serif
Other font styles liked:
• Tahoma, Verdana, Calibri

Requirements
Must have
• MUST MEET NORVEXA.example GUIDLINES ;
• File Types
• Lumira Author Hub currently accepts two types of files for cover images:
• JPEG (JPEG / JPG)
• TIFF (TIF / TIFF)
• We apply additional compression to images when displaying them on the website. For best results, please upload your images with minimal compression.
• Dimensions
• Requirements for the size of your cover art must have an ideal height/width ratio of at least 8:5 (1.6), meaning:
• • A minimum of 625 pixels on the shortest side and 1000 pixels on the longest side
• • For best quality, your image should be 2500 pixels on the longest side
• Important: We cannot accept any images larger than 10,000 pixels on the longest side.
• Size
• Your cover image must be less than 50MB. If the file type you are using supports compression, make sure to enable as little compression as possible, e.g. none for TIFF. Be sure to save your file with 72 dots per inch (DPI).
• Color
• Product images display on the Norvexa website using the RGB (red, green, blue) color mode or profile. RGB is the color mode native to the web and many color screen displays, as these three colors displayed at varying levels of intensity create over 16 million colors. When saving and uploading your cover image file, save your file ONLY as RGB - not CMYK or sRGB- for the color profile. You can usually find this option in the File saving dialog of image manipulation programs such as Photoshop.
• Some programs may also refer to RGB color as 'True Color' in some programs. If in doubt, try opening a JPG inside Internet Explorer, Firefox, or Safari. If a JPG opens fine inside a web browser, it's most likely okay to use as a cover image.
• Make sure to save your image without color separation. This is usually a pre-press or color palette option. Use your image manipulation program or image analysis tool (some are available free online) to verify that your image file doesn't have color separation.
• Use color images whenever possible and relevant. In addition to the Lumira black and white Z Slate reading devices, customers can read your books on full color Tessel devices and free Lumira reading apps for iPhone, iPad, Android, PC or Mac.
Should not have
• NO MALE OR FEMALE MODLES OR HALF NAKED PEOPLE...

```html
<!DOCTYPE html>
<html lang="en">
<head>
<meta charset="utf-8">
<title>Steady Frame Slim Down Roadmap – eBook Cover</title>
<link rel="stylesheet" href="https://fonts.googleapis.com/css2?family=Open+Sans:wght@400;500&display=swap">
<style>
  :root {
    --bg-centre: #fbfbfb;
    --bg-edge: #dedede;
    --ink-dark: #3a3a3a;
    --ink-body: #2e2e2e;
    --olive-light: #a6b21c;
    --olive-dark: #86940e;
    --gold: #e9c225;
    --heart-green: #6f9a3a;
    --heart-yellow: #e8bd2c;
    --heart-orange: #e46a1e;
    --heart-red: #c8231c;
  }
  html, body {
    margin: 0;
    padding: 0;
    overflow: hidden;
  }
  .cover {
    position: relative;
    width: 750px;
    height: 1200px;
    overflow: hidden;
    background: radial-gradient(ellipse at 50% 45%, var(--bg-centre) 0%, #f2f2f2 55%, var(--bg-edge) 100%);
    font-family: "Open Sans", Verdana, sans-serif;
    text-align: center;
  }
  .line {
    position: absolute;
    left: 0;
    width: 100%;
    margin: 0;
    line-height: 1;
    white-space: nowrap;
  }
  .title-top {
    top: 34px;
    font-size: 92px;
    font-weight: 400;
    color: var(--ink-dark);
    letter-spacing: -0.01em;
  }
  .title-main {
    top: 110px;
    font-size: 142px;
    font-weight: 500;
    color: var(--ink-body);
    letter-spacing: -0.02em;
  }
  .food-heart {
    position: absolute;
    left: 156px;
    top: 292px;
    width: 440px;
    height: 372px;
  }
  .subtitle-one {
    top: 676px;
    font-size: 168px;
    font-weight: 400;
    color: var(--olive-dark);
    background: linear-gradient(180deg, var(--olive-light), var(--olive-dark));
    -webkit-background-clip: text;
    background-clip: text;
    -webkit-text-fill-color: transparent;
  }
  .subtitle-two {
    top: 818px;
    font-size: 150px;
    font-weight: 400;
    color: var(--olive-dark);
    letter-spacing: -0.02em;
    background: linear-gradient(180deg, var(--olive-light), var(--olive-dark));
    -webkit-background-clip: text;
    background-clip: text;
    -webkit-text-fill-color: transparent;
  }
  .subtitle-three {
    top: 978px;
    font-size: 80px;
    font-weight: 400;
    color: var(--gold);
    letter-spacing: 0.2em;
    text-indent: 0.2em;
  }
  .author {
    top: 1116px;
    font-size: 42px;
    font-weight: 400;
    color: var(--ink-dark);
    letter-spacing: 0.24em;
    text-indent: 0.24em;
  }
</style>
</head>
<body>
  <main class="cover">
    <h1 class="line title-top">STEADY</h1>
    <p class="line title-main">FRAME</p>

    <svg class="food-heart" viewBox="0 0 100 90" role="img" aria-label="Heart shape arranged from fresh fruit, vegetables, bread and salmon">
      <defs>
        <linearGradient id="produce-tones" x1="0" y1="0" x2="1" y2="1">
          <stop offset="0" stop-color="var(--heart-green)"/>
          <stop offset="0.4" stop-color="var(--heart-yellow)"/>
          <stop offset="0.7" stop-color="var(--heart-orange)"/>
          <stop offset="1" stop-color="var(--heart-red)"/>
        </linearGradient>
      </defs>
      <path d="M50 88 C30 72 2 52 2 26 C2 11 13 2 26 2 C37 2 45 9 50 18 C55 9 63 2 74 2 C87 2 98 11 98 26 C98 52 70 72 50 88 Z" fill="url(#produce-tones)"/>
    </svg>

    <p class="line subtitle-one">SLIM</p>
    <p class="line subtitle-two">DOWN</p>
    <p class="line subtitle-three">ROADMAP</p>
    <p class="line author">AUTHOR’S NAME</p>
  </main>
</body>
</html>
```